Brookfarrow Osteopathy and dry needling business card

Business card for Brookfarrow Osteopathy and Dry Needling.

Industry/Entity Type

Health

Contact Information for Business Card

I do not have a phone number yet. I also do not have an email address yet. The physical address is: 48 Lower Crane Street Brookfarrow The website is: www.brookfarrowosteosteopathy.example My details are: Dr Martin Pellowe, Osteopath (B.Clin.Sci (Ost) M.Ost BSC ECON (Hons)

Colors
0094D4
00A9DD
6FCCEA
C7EBF8
E9F6FB

Requirements
Must have
• logo on the back
Nice to have
• Maybe a space for me to write an appointment time and date on the card.

```html
<!DOCTYPE html>
<html lang="en">
<head>
<meta charset="utf-8">
<title>Brookfarrow Osteopathy and Dry Needling – Business Card</title>
<link rel="stylesheet" href="https://fonts.googleapis.com/css2?family=Montserrat:wght@500;700&family=Mulish:wght@300;400&display=swap">
<style>
  :root {
    --brand-blue: #0094d4;
    --brand-orange: #f7901e;
    --ink-grey: #777777;
    --label-grey: #6d6d6d;
    --rule-grey: #9a9a9a;
    --card-white: #ffffff;
    --backdrop: #b4b4b4;
    --soft-white: rgba(255,255,255,0.75);
  }
  * { box-sizing: border-box; margin: 0; padding: 0; }
  html, body { width: 1200px; height: 1000px; overflow: hidden; }
  body { background: var(--backdrop); position: relative; font-family: "Mulish", sans-serif; }

  .card {
    position: absolute; left: 316px; width: 568px; height: 327px;
    border-radius: 29px; overflow: hidden;
  }
  .card--front { top: 147px; background: var(--brand-blue); }
  .card--back { top: 527px; background: var(--card-white); }

  /* Front */
  .brand-mark {
    position: absolute; left: 190px; top: 65px; width: 188px; height: 188px;
    border: 2px solid var(--card-white); border-radius: 50%;
    display: flex; align-items: center; justify-content: center; text-align: center;
  }
  .brand-mark__name {
    font-family: "Montserrat", sans-serif; font-weight: 500; font-size: 15px;
    line-height: 1.35; letter-spacing: 1.5px; text-transform: uppercase; color: var(--card-white);
  }
  .web-address {
    font-family: "Montserrat", sans-serif; font-weight: 700; white-space: nowrap;
  }
  .web-address__domain { color: inherit; }
  .web-address__service { color: var(--brand-orange); }
  .web-address__tld { font-weight: 400; }
  .card--front .web-address {
    position: absolute; left: 0; right: 0; top: 278px; text-align: center;
    font-size: 18.5px; color: var(--card-white);
  }
  .card--front .web-address__tld { color: var(--soft-white); }

  /* Back – practitioner */
  .practitioner { position: absolute; left: 33px; top: 50px; width: 230px; }
  .practitioner__name {
    font-family: "Montserrat", sans-serif; font-weight: 700; font-size: 29px; line-height: 34px;
  }
  .practitioner__first { color: var(--brand-blue); display: block; }
  .practitioner__last { color: var(--brand-orange); display: block; }
  .practitioner__credentials {
    font-family: "Montserrat", sans-serif; font-weight: 500; font-size: 13.5px; line-height: 16px;
    color: #8e8e8e; margin-top: 5px;
  }
  .contact-list { position: absolute; left: 33px; top: 187px; list-style: none; }
  .contact-list li {
    display: flex; align-items: center; gap: 6px; font-size: 18px; font-weight: 300;
    color: var(--ink-grey); height: 25px;
  }
  .contact-icon { width: 20px; height: 20px; flex: none; }
  .contact-divider {
    position: absolute; left: 33px; top: 246px; width: 197px; height: 2px; background: var(--brand-orange);
  }
  .address {
    position: absolute; left: 34px; top: 257px; font-style: normal; font-weight: 300;
    font-size: 17px; line-height: 21px; color: var(--ink-grey);
  }

  /* Back – appointment */
  .appointment { position: absolute; left: 284px; top: 0; width: 248px; height: 100%; }
  .appointment__field { position: absolute; left: 0; width: 245px; height: 30px; }
  .appointment__field--date { top: 52px; }
  .appointment__field--time { top: 92px; }
  .appointment__label {
    font-family: "Montserrat", sans-serif; font-weight: 700; font-size: 22px; color: var(--label-grey);
    position: absolute; left: 0; bottom: -4px;
  }
  .appointment__line {
    position: absolute; left: 54px; right: 0; bottom: 0; height: 1px; background: var(--rule-grey);
  }
  .appointment__sep {
    position: absolute; left: 128px; bottom: 2px; font-size: 18px; font-weight: 300; color: var(--ink-grey);
  }
  .weekdays { position: absolute; left: 0; top: 143px; display: flex; gap: 21px; list-style: none; }
  .weekdays li {
    width: 23px; height: 22px; border: 1px solid var(--label-grey);
    font-size: 13px; color: var(--label-grey); display: flex; align-items: center; justify-content: center;
  }
  .appointment__notice {
    position: absolute; left: -20px; right: -20px; top: 190px; text-align: center;
    font-size: 16px; font-weight: 300; line-height: 21.5px; color: var(--ink-grey);
  }
  .card--back .web-address {
    position: absolute; left: -10px; right: -10px; top: 275px; text-align: center; font-size: 14px;
  }
  .card--back .web-address__domain { color: var(--brand-blue); }
  .card--back .web-address__tld { color: #999999; }
</style>
</head>
<body>

<section class="card card--front" aria-label="Card front">
  <div class="brand-mark">
    <p class="brand-mark__name">Brookfarrow<br>Osteopathy<br>&amp; Dry Needling</p>
  </div>
  <p class="web-address"><span class="web-address__domain">brookfarrow</span><span class="web-address__service">osteosteopathy</span><span class="web-address__tld">.example</span></p>
</section>

<section class="card card--back" aria-label="Card back">
  <div class="practitioner">
    <h1 class="practitioner__name">
      <span class="practitioner__first">DR. MARTIN</span>
      <span class="practitioner__last">PELLOWE</span>
    </h1>
    <p class="practitioner__credentials">Osteopath (B.Clin.Sci (Ost)<br>M.Ost BSC ECON (Hons)</p>
  </div>

  <ul class="contact-list">
    <li>
      <svg class="contact-icon" viewBox="0 0 20 20" aria-hidden="true">
        <circle cx="10" cy="10" r="10" fill="#f7901e"/>
        <path d="M7 5.2l1.6 2.4-1 1.1c.7 1.4 1.7 2.4 3 3.1l1.1-1 2.4 1.6-.8 1.8c-3.6.3-7.4-3.6-7.1-7.3z" fill="#fff"/>
      </svg>
      123 45678
    </li>
    <li>
      <svg class="contact-icon" viewBox="0 0 20 20" aria-hidden="true">
        <circle cx="10" cy="10" r="10" fill="#f7901e"/>
        <g fill="none" stroke="#fff" stroke-width="1">
          <circle cx="10" cy="10" r="5"/>
          <ellipse cx="10" cy="10" rx="2.2" ry="5"/>
          <path d="M5 10h10M5.8 7.5h8.4M5.8 12.5h8.4"/>
        </g>
      </svg>
      email@website.com
    </li>
  </ul>
  <div class="contact-divider"></div>
  <address class="address">48 Lower Crane Street<br>Brookfarrow</address>

  <div class="appointment">
    <div class="appointment__field appointment__field--date">
      <span class="appointment__label">Date</span>
      <span class="appointment__sep">/</span>
      <span class="appointment__line"></span>
    </div>
    <div class="appointment__field appointment__field--time">
      <span class="appointment__label">Time</span>
      <span class="appointment__sep">:</span>
      <span class="appointment__line"></span>
    </div>
    <ul class="weekdays">
      <li>M</li><li>T</li><li>W</li><li>T</li><li>F</li><li>S</li>
    </ul>
    <p class="appointment__notice">If your unable to keep your<br>appointment, kindly give us<br>24 hour notice</p>
    <p class="web-address"><span class="web-address__domain">brookfarrow</span><span class="web-address__service">osteosteopathy</span><span class="web-address__tld">.example</span></p>
  </div>
</section>

</body>
</html>
```